Business card design needed with logo

My business is called KVM Solutions & it is targeted towards mobile equipment maintenance in the Mining and civil industry. My work involves maintenance planning and maintenance management plus also supply tradespeople on a labour hire basis. We can provide from basic shut-down machine rebuild plans to complete rebuild services supply plans and labour to anywhere in Australia. I would like to use the colours Black, Red and Grey, I had done a desgin as attached but doesn't really explain what we do and gears don't embroider well onto shirts.
Updates

I also wanted to see the something replace the gears maybe just making the KVM lettering look a bit different or put together differently 

Hello I have extended the deadline by a few extra days as I would like to update details on the front of card, details below & can be put which ever way looks good;

Liam Fenwick
Director
0417263958
KVM@mailnest.com.au
www.kvmsolutions-demo.com.au

On the back of the card I would like to have the below printed;

Capable of providing, but not limited to, across Australia:
- Contract Maintenance Planning.
- Skilled Mobile Maintenance labour hire.
- New machine build specifications. 
- Plant risk assessments and inspections.
- Shut down and rebuild program planning.
- Preventative maintenance tasks, including build of materials lists, creation and review.

Target Market(s)

Contractors and companies that use small and large earthmoving and mining machines

Industry/Entity Type

Business

Contact Information for Business Card

Trading name is KVM Solutions
My name and title is
Liam Fenwick Director
0417 263 958
KVM@mailnest.com.au

Logo Text

KVM

```html
<!DOCTYPE html>
<html lang="en">
<head>
<meta charset="utf-8">
<title>KVM Solutions – Business Card</title>
<link rel="stylesheet" href="https://fonts.googleapis.com/css2?family=Ubuntu:wght@300;400&display=swap">
<style>
  :root {
    --page-bg: #ffffff;
    --page-frame: #1a1a1a;
    --front-dark: #0c2a30;
    --front-blue-top: #177aa3;
    --front-blue-bottom: #0b4f97;
    --back-blue-top: #3a8cbc;
    --back-blue-bottom: #2262b0;
    --back-edge: #4a5560;
    --text-light: #ffffff;
  }
  * { box-sizing: border-box; margin: 0; padding: 0; }
  html, body {
    width: 1016px;
    height: 1200px;
    overflow: hidden;
    background: var(--page-bg);
  }
  .sheet {
    position: relative;
    width: 1016px;
    height: 1200px;
    border: 1.5px solid var(--page-frame);
    font-family: "Ubuntu", "Helvetica Neue", Arial, sans-serif;
    font-weight: 300;
    color: var(--text-light);
  }
  .card {
    position: absolute;
    left: 55px;
    width: 899px;
    height: 513px;
    overflow: hidden;
  }
  /* Front */
  .card--front {
    top: 49px;
    background: var(--front-dark);
    border: 1px solid #000;
  }
  .front-panel {
    position: absolute;
    left: 478px;
    top: 0;
    width: 387px;
    height: 100%;
    background: linear-gradient(to bottom, var(--front-blue-top), var(--front-blue-bottom));
  }
  .contact {
    position: absolute;
    left: 102px;
    top: 186px;
    font-size: 29px;
    line-height: 34px;
    letter-spacing: 0.3px;
  }
  .brand-name {
    position: absolute;
    font-weight: 300;
    color: var(--text-light);
    white-space: nowrap;
  }
  .brand-name--front {
    right: 24px;
    top: 224px;
    font-size: 42px;
  }
  .web {
    position: absolute;
    font-size: 23px;
    letter-spacing: 0.3px;
    white-space: nowrap;
  }
  .web--front {
    right: 24px;
    top: 456px;
  }
  /* Back */
  .card--back {
    top: 636px;
    background: linear-gradient(to bottom, var(--back-blue-top), var(--back-blue-bottom));
    border: 1px solid var(--back-edge);
  }
  .brand-name--back {
    right: 34px;
    top: 58px;
    font-size: 56px;
  }
  .services {
    position: absolute;
    left: 36px;
    top: 174px;
    list-style: none;
    font-size: 29px;
    line-height: 34px;
    letter-spacing: 0.2px;
  }
  .services li {
    padding-left: 21px;
    text-indent: -21px;
  }
  .services li::before { content: "- "; }
  .web--back {
    right: 22px;
    top: 455px;
    font-size: 25px;
  }
</style>
</head>
<body>
  <main class="sheet">
    <section class="card card--front" aria-label="Card front">
      <div class="front-panel">
        <div class="brand-name brand-name--front">KVM Solutions</div>
        <div class="web web--front">www.kvmsolutions-demo.com.au</div>
      </div>
      <div class="contact">
        <p class="contact-name">Liam Fenwick</p>
        <p class="contact-title">Director</p>
        <p class="contact-phone">0417263958</p>
        <p class="contact-email">KVM@mailnest.com.au</p>
      </div>
    </section>

    <section class="card card--back" aria-label="Card back">
      <div class="brand-name brand-name--back">KVM Solutions</div>
      <ul class="services">
        <li>Contract Maintenance Planning.</li>
        <li>Skilled Mobile Maintenance labour hire.</li>
        <li>New machine build specifications.</li>
        <li>Plant risk assessments and inspections.</li>
        <li>Shut down and rebuild program planning.</li>
        <li>Preventative maintenance tasks, including build of materials lists, creation and review.</li>
      </ul>
      <div class="web web--back">www.kvmsolutions-demo.com.au</div>
    </section>
  </main>
</body>
</html>
```